Beautiful Quotes For Social Media Posts

We are looking for 5 beautifully designed quotes for our social media account.

Inspiration of styles we like in both style and color along with a few of our favorite fonts (you are NOT limited to these fonts this is just to give you an idea):
https://quillmorestudio.example.com/s/k7p2vx9tqa41mzn8wbd3ce6hr5lf0y2j

*These fonts are property of Quillmore Studio. You do not have permission/rights to use them outside of this assignment*

Quotes to use (5):
“Only those who dare to fail greatly can ever achieve greatly.” –Vernon T. Ashgrove
“Don’t go through life, grow through life.” – Milo Pendrake
“Follow your bliss and the universe will open doors where there were only walls.” – Arthur Venholm
“If you don’t like the road you’re walking, start paving another one.” – Greta Mossley
“Life is like riding a bicycle. To keep your balance, you must keep moving.” —Lucian Thornwick

File Specifics:
- JPG
- 10x10 in size (square)
- Please include @QuillmoreStudio in the bottom right left or center of each design

Brand Details:
Soft but rich pastel and bright colors.
Hand Drawn florals, doodles and art
Handwritten looking fonts
Artsy, Creative, Girl and Inspiring

```html
<!DOCTYPE html>
<html lang="en">
<head>
<meta charset="utf-8">
<title>Follow Your Bliss – Quote Post</title>
<link href="https://fonts.googleapis.com/css2?family=Kaushan+Script&family=Montserrat:wght@600&display=swap" rel="stylesheet">
<style>
  :root {
    --navy: #323a50;
    --paper: #ffffff;
    --gold: #d9a63c;
    --gold-light: #efc866;
    --ink: #111111;
    --rose: #f2a3cf;
    --rose-deep: #e46fb2;
    --leaf: #6fa567;
  }
  html, body {
    margin: 0;
    padding: 0;
    width: 1200px;
    height: 1200px;
    overflow: hidden;
  }
  .post {
    position: relative;
    width: 1200px;
    height: 1200px;
    overflow: hidden;
    background: repeating-linear-gradient(
      to bottom,
      var(--navy) 0 58px,
      var(--paper) 58px 122px
    );
  }
  .quote-card {
    position: absolute;
    left: 139px;
    top: 133px;
    width: 922px;
    height: 923px;
    box-sizing: border-box;
    background: var(--paper);
    border: 13px solid var(--gold);
    outline: 3px dotted var(--gold-light);
    outline-offset: -8px;
  }
  .quote-text {
    position: absolute;
    left: 139px;
    top: 300px;
    width: 922px;
    margin: 0;
    text-align: center;
    font-family: "Kaushan Script", cursive;
    font-weight: 400;
    font-size: 80px;
    line-height: 133px;
    color: var(--ink);
  }
  .handle {
    position: absolute;
    left: 0;
    width: 1200px;
    top: 950px;
    text-align: center;
    font-family: "Montserrat", sans-serif;
    font-weight: 600;
    font-size: 29px;
    color: var(--ink);
  }
  .floral {
    position: absolute;
    border-radius: 50%;
  }
  .floral--top-left {
    left: -40px;
    top: -30px;
    width: 540px;
    height: 500px;
    background: radial-gradient(ellipse at 40% 40%, var(--rose) 0%, var(--rose-deep) 25%, rgba(111,165,103,0.8) 50%, rgba(111,165,103,0) 70%);
  }
  .floral--bottom-right {
    left: 710px;
    top: 740px;
    width: 540px;
    height: 500px;
    background: radial-gradient(ellipse at 55% 55%, var(--rose) 0%, var(--rose-deep) 25%, rgba(111,165,103,0.8) 50%, rgba(111,165,103,0) 70%);
  }
  .sparkles {
    position: absolute;
    inset: 0;
    pointer-events: none;
  }
</style>
</head>
<body>
  <main class="post">
    <div class="quote-card"></div>

    <svg class="sparkles" width="1200" height="1200" viewBox="0 0 1200 1200" aria-hidden="true">
      <g fill="var(--gold)">
        <circle cx="977" cy="39" r="26"/>
        <circle cx="612" cy="70" r="24"/>
        <circle cx="1108" cy="260" r="25"/>
        <circle cx="1174" cy="500" r="24"/>
        <circle cx="92" cy="520" r="20"/>
        <circle cx="60" cy="740" r="30"/>
        <circle cx="1106" cy="750" r="26"/>
        <circle cx="47" cy="1070" r="28"/>
        <circle cx="333" cy="1150" r="22"/>
        <circle cx="615" cy="1113" r="26"/>
        <circle cx="950" cy="1172" r="24"/>
      </g>
    </svg>

    <div class="floral floral--top-left" role="img" aria-label="Hand-painted pink roses with green leaves and curling vines"></div>
    <div class="floral floral--bottom-right" role="img" aria-label="Hand-painted pink roses with green leaves, vines and coral berry sprigs"></div>

    <p class="quote-text">Follow your bliss and<br>the universe will open<br>doors where there<br>were only walls</p>

    <div class="handle">@QuillmoreStudio</div>
  </main>
</body>
</html>
```